Business Card Design for Vintage Jazz

I am a vintage jazz band leader in New York City. My groups play the music of the 1920s, 1930s and 1940s. My website is marlowpeskin.com for more info on what I do.

I am looking for a two sided business card design that has the look and feel of a really nice business card from the 1930s. I need to convey with the design that my work has that vintage kind of class and style, but also conveys that we are fun and entertaining.

Most importantly it should make a bold staement. If Hollis Varnum had a card, what would it have looked like? I want a card that I feel confident will make an impact and will let people know that my work is te the top that NYC has to offer in vintage jazz..

Note that I have only decided to avoid the "committed payment" option as I have not used this service before. Assuming that I get quality work I will select a design from those presented.

Target Market(s)

people who want to hire my band for events, media, and new fans of the band

Industry/Entity Type

Performing Art

Contact Information for Business Card

Definitely a matte finish, possibly a sort of old style of paper with that brown tint? definitely a thick card.

Requirements
Must have
• FRONT
• My name: Marlow Peskin
• What I do: Bandleader, Guitarist, Vocalist, Songwriter
• Contact Details: marlowpeskin.com marlow@marlowpeskin.com 646-555-0187
• BACK
• My Social Media Links:
• facebook.marlowpeskin.com
• twitter, instagram, linkedin: marlowpeskin
• I'm also including a photo image I would like to use. The photo's background is not needed, and to be honest isn't really desireable. Just looking to use the image of me.
Nice to have
• I'm attaching which could be used as is, omitted from the card, or altered maybe with text going around the outside of the circle or in some other way. It may need some clean up to the edges of the lettering as we only use it for the website thumbnail.
• If there's space I'd like to include the text "join our mailing list for a free song download: freesong.marlowpeskin.com" If not perhaps just "Download a Free Song at: freesong.marlowpeskin.com - something to this end.
Should not have
• anything cartoony. Don't think retro 90s's vision of the swing era, think actual swing era!
• anything modern. Got to look old school
• Try to avoid dark backgrounds. Since we often play in bars and clubs where it is dar, a d
• avoid script fonts.

```html
<!DOCTYPE html>
<html lang="en">
<head>
<meta charset="utf-8">
<title>Marlow Peskin – Business Card</title>
<link rel="stylesheet" href="https://fonts.googleapis.com/css2?family=Arimo:wght@400;700&display=swap">
<style>
  :root {
    --stage: #e9e7e3;
    --paper: #ffffff;
    --ink: #111111;
    --ink-soft: #333333;
    --grey-text: #3a3a3a;
    --teal: #5cbfa6;
    --photo-dark: #3c3c3c;
    --card-shadow: 0 6px 18px rgba(0,0,0,0.18);
  }
  * { box-sizing: border-box; margin: 0; padding: 0; }
  html, body {
    width: 1200px; height: 902px; overflow: hidden;
    background: var(--stage);
    font-family: "Arimo", Arial, sans-serif;
  }
  .stage {
    width: 1200px; height: 902px;
    display: flex; flex-direction: column; align-items: center; justify-content: center;
    gap: 22px;
  }
  .card {
    position: relative;
    width: 740px; height: 423px;
    background: var(--paper);
    box-shadow: var(--card-shadow);
    overflow: hidden;
  }

  /* Back side */
  .card-back .mark {
    position: absolute; left: 48px; top: 120px;
    display: flex; align-items: center; gap: 26px;
  }
  .card-back .mark-circle {
    width: 180px; height: 180px; border-radius: 50%;
    background: var(--ink);
  }
  .card-back .mark-name {
    font-weight: 700; font-size: 40px; color: var(--ink);
    letter-spacing: 0.5px;
  }
  .card-back .site {
    position: absolute; left: 254px; top: 232px;
    font-size: 30px; color: var(--grey-text);
  }
  .card-back .social-square {
    position: absolute; right: 92px; top: 58px;
    width: 28px; height: 28px; background: var(--ink);
  }

  /* Front side */
  .card-front .shapes { position: absolute; inset: 0; }
  .card-front .portrait {
    position: absolute; left: 60px; top: 90px;
    width: 300px; height: 333px;
    background: linear-gradient(180deg, rgba(230,230,230,0.55) 0%, var(--photo-dark) 60%, #1e1e1e 100%);
    clip-path: polygon(30% 0, 62% 0, 78% 20%, 100% 30%, 100% 100%, 8% 100%, 12% 30%);
    opacity: 0.85;
  }
  .card-front .identity {
    position: absolute; right: 36px; top: 46px;
    text-align: right; color: var(--ink);
  }
  .card-front .name { font-weight: 700; font-size: 36px; }
  .card-front .role {
    margin-top: 8px; font-weight: 700; font-size: 19px; line-height: 1.15; color: var(--ink-soft);
  }
  .card-front .contacts {
    position: absolute; right: 28px; top: 252px;
    list-style: none; color: #fff; text-align: right;
  }
  .card-front .contacts li {
    display: flex; justify-content: flex-end; align-items: center; gap: 14px;
    font-size: 21px; line-height: 30px;
  }
  .card-front .icon {
    width: 18px; height: 18px; background: #fff; display: inline-flex;
    align-items: center; justify-content: center;
  }
</style>
</head>
<body>
<main class="stage">

  <section class="card card-back" aria-label="Card back">
    <div class="mark">
      <span class="mark-circle"></span>
      <span class="mark-name">Marlow Peskin</span>
    </div>
    <p class="site">marlowpeskin.com</p>
    <span class="social-square"></span>
  </section>

  <section class="card card-front" aria-label="Card front">
    <svg class="shapes" width="740" height="423" viewBox="0 0 740 423">
      <polygon points="0,0 178,0 420,228 420,423 0,423" fill="var(--teal)"/>
      <polygon points="420,228 740,228 740,423 420,423" fill="var(--ink)"/>
      <line x1="184" y1="-2" x2="428" y2="228" stroke="var(--ink)" stroke-width="5"/>
    </svg>
    <div class="portrait" role="img" aria-label="Photo of the bandleader in a dark blazer tipping a straw boater hat"></div>

    <div class="identity">
      <h1 class="name">Marlow Peskin</h1>
      <p class="role">Bandleader, Guitarist,<br>Vocalist, Songwriter</p>
    </div>

    <ul class="contacts">
      <li>646-555-0187
        <span class="icon"><svg width="12" height="12" viewBox="0 0 12 12"><path d="M2 1h3l1 3-2 1a7 7 0 0 0 3 3l1-2 3 1v3c-6 0-9-3-9-9z" fill="#111"/></svg></span>
      </li>
      <li>marlowpeskin.com
        <span class="icon"><svg width="12" height="12" viewBox="0 0 12 12"><circle cx="6" cy="6" r="5" fill="none" stroke="#111" stroke-width="1.3"/><path d="M1 6h10M6 1c-3 3-3 7 0 10M6 1c3 3 3 7 0 10" fill="none" stroke="#111" stroke-width="1"/></svg></span>
      </li>
      <li>marlow@marlowpeskin.com
        <span class="icon"><svg width="12" height="12" viewBox="0 0 12 12"><rect x="1" y="3" width="10" height="7" fill="none" stroke="#111" stroke-width="1.3"/><path d="M1 3l5 4 5-4" fill="none" stroke="#111" stroke-width="1.2"/></svg></span>
      </li>
    </ul>
  </section>

</main>
</body>
</html>
```